Corvelle Beauty Lounge needs a product poster

This poster is advertising our products and services. There are several damask patterns throughout the store. Our store's colors are blue, yellow, white, and gold.However the use of vibrant colors would be great! Our theme is old Hollywood. We have to use this design for our price list, product advertisement, and store promotions poster. Poster 2 and 3 can have the same layout. Poster 1 is different because I want the menu enclosed in a frame with the model resting against it or on top of it. All three posters will be hung on the same wall. I have attached my logo and additional photos for your review. I have also attached a images few posters. To give a better idea. I like how the fonts are not all the same. I like how they used the space. I like the use of color. Also I want the logo small with a white oval background. I don't want our logo to be a focal point.
Poster 1: The menu. This poster should include the blonde sailor either above the menu or beside the menu, 2 images have been included to choose from. I want the area with the prices in some type of decorative frame, with the model on top or on the side. (The model is displaying the prices) Also the model's background is white but I want her background to have color. Green would be great! I also like the idea of having "Now Showing" as part of the frame.
The text should read
" Services
Full Body Application..........................................$35.00
Half Body Application.........................................$20.00
Competition Application......................................$50,00
Face Only...........................................................$10.00
Packages:
4 Tans.... ............................................................$120.00 (Never Expires)
8 Tans ................................................................$200.00 (Never Expires)
Monthly Unlimited...............................................$95.00
Specials:
High School Students .......................................$25.00 EVERYDAY!!
All Day Every Tuesday.......................................$25.00
New Clients........................................................$25.00 (First Visit Only)
(If you want to be creative this section can be separate from the menu or part of the menu. Your choice)
Don't have time to come to us? We also have MOBILE Services! OUR ARTISTS CAN COME TO YOU!
In-Home Party Rates (5 people or more)...........$35.00 per person (Travel Fee Waived)
Poster 2: Kelvane Solution...The image of the pinup with the clock if for this poster.
The text should read:
" PRESSED FOR TIME? Try our KELVANE sunless solution. Rinse in as little as 2 hours" (Pressed for time, Kelvane, and 2 Hours is what we want to stand out)
Poster 3: Packages..The image for this poster is of the girl with the binoculars.
The text should read:
"We offer packages and memberships with UNBELIEVABLE SAVINGS. Tans as low as $20!!" (Unbelievable savings and $20 is what we want to stand out)
I made changes to my briefing. Please let me know if I need to make any other changes or additions
We increased our budget for our design, in order to get more participants
I updated our brief. I have included examples and more detailed instructions. I hope this helps
People who value beauty and glamour. We have an upscale clientele.
Advertising

```html
<!DOCTYPE html>
<html lang="en">
<head>
<meta charset="utf-8">
<title>Corvelle Beauty Lounge – Poster Series</title>
<link href="https://fonts.googleapis.com/css2?family=Arvo:wght@400;700&family=Cinzel:wght@700&family=Playfair+Display+SC:wght@400;700&family=Lora:wght@500&display=swap" rel="stylesheet">
<style>
  :root {
    --backdrop: #e4e4e4;
    --ink: #1e1e1e;
    --paper: #ffffff;
    --sky: #1fa8e6;
    --sky-dark: #1b86c4;
    --lemon: #f6f13a;
    --gold: #c9a24a;
    --brand: #7a3a97;
    --green-top: #7fcf8f;
    --green-bottom: #2f8f55;
    --ice-top: #f3f8fb;
    --ice-bottom: #bfdfee;
    --charcoal: #262424;
    --blush: #f2a7ad;
    --navy: #3a5598;
    --label: #1c1c1c;
  }
  * { box-sizing: border-box; margin: 0; padding: 0; }
  html, body { width: 1200px; height: 600px; overflow: hidden; }
  body { background: var(--backdrop); font-family: "Arvo", serif; color: var(--ink); position: relative; }

  .series-label { position: absolute; top: 46px; font-family: "Lora", serif; font-weight: 500; font-size: 19px; color: var(--label); }

  .poster { position: absolute; top: 79px; width: 342px; height: 481px; overflow: hidden; }
  .poster--menu { left: 40px; background: var(--paper); }
  .poster--solution { left: 433px; background: linear-gradient(180deg, var(--ice-top), var(--ice-bottom)); }
  .poster--packages { left: 818px; background: var(--blush); }

  .brand-name { position: absolute; font-family: "Cinzel", serif; font-weight: 700; font-size: 17px; color: var(--brand); letter-spacing: 1px; }
  .poster--menu .brand-name { right: 12px; top: 16px; }
  .poster--packages .brand-name { right: 14px; top: 22px; }
  .poster--solution .brand-name { left: 14px; top: 14px; }

  /* Poster 1 – menu */
  .menu-topbar { position: absolute; top: 0; left: 0; width: 100%; height: 8px; background: var(--sky); }
  .model-photo--sailor { position: absolute; left: 248px; top: 44px; width: 94px; height: 348px; background: linear-gradient(180deg, var(--green-top), var(--green-bottom)); }
  .menu-frame { position: absolute; left: 8px; top: 16px; width: 234px; height: 366px; border: 4px double var(--gold); outline: 1px solid var(--sky-dark); outline-offset: -9px; }
  .now-showing { position: absolute; left: 8px; top: 24px; width: 234px; text-align: center; font-family: "Cinzel", serif; font-size: 11px; letter-spacing: 3px; color: var(--gold); }
  .menu-heading { position: absolute; left: 30px; width: 190px; text-align: center; font-family: "Cinzel", serif; font-size: 14px; color: var(--ink); }
  .menu-heading::before, .menu-heading::after { content: ""; position: absolute; left: 24px; right: 24px; height: 2px; background: var(--sky-dark); }
  .menu-heading::before { top: -5px; }
  .menu-heading::after { bottom: -4px; }
  .menu-line { position: absolute; left: 18px; font-size: 10px; white-space: nowrap; }
  .mobile-band { position: absolute; left: 0; top: 392px; width: 100%; height: 89px; background: var(--sky); text-align: center; }
  .mobile-band p { position: absolute; left: 0; width: 100%; color: var(--paper); }
  .mobile-band .mobile-note { top: 8px; font-size: 9.5px; }
  .mobile-band .mobile-call { top: 24px; font-size: 13.5px; }
  .mobile-band .party-rate { color: var(--lemon); font-size: 12px; }

  /* Poster 2 – solution */
  .solution-title { position: absolute; left: 0; width: 100%; text-align: center; font-family: "Playfair Display SC", serif; font-weight: 700; color: var(--ink); letter-spacing: 2px; text-shadow: 2px 2px 0 #b9c3c8; font-size: 30px; }
  .solution-title--first { top: 44px; padding-left: 40px; }
  .solution-title--second { top: 94px; }
  .model-photo--clock { position: absolute; left: 0; top: 152px; width: 342px; height: 255px; background: linear-gradient(160deg, #d9e7ee 0%, #c8a89a 45%, #b8323a 80%); }
  .solution-band { position: absolute; left: 0; top: 407px; width: 100%; height: 74px; background: var(--charcoal); color: var(--paper); text-align: center; font-size: 12px; }
  .solution-band p { position: absolute; left: 0; width: 100%; }

  /* Poster 3 – packages */
  .model-photo--binoculars { position: absolute; left: 0; top: 0; width: 342px; height: 350px; background: linear-gradient(180deg, #f2b3b3 0%, #d9c9d6 50%, #6a86b8 100%); }
  .low-price { position: absolute; left: 172px; top: 88px; width: 80px; text-align: center; color: var(--ink); font-weight: 700; }
  .low-price .low-price-lead { font-size: 13px; line-height: 1.15; }
  .low-price .low-price-amount { font-size: 27px; color: var(--paper); text-shadow: 1px 1px 0 var(--ink), -1px -1px 0 var(--ink), 1px -1px 0 var(--ink), -1px 1px 0 var(--ink); }
  .savings-band { position: absolute; left: 0; top: 355px; width: 100%; height: 118px; background: var(--navy); border-top: 4px solid var(--paper); border-bottom: 4px solid var(--paper); box-shadow: 0 -8px 0 -4px var(--navy); text-align: center; color: var(--paper); font-family: "Lora", serif; font-weight: 500; font-size: 22px; line-height: 31px; padding-top: 10px; }
  .savings-band strong { font-weight: 500; letter-spacing: 0.5px; }
</style>
</head>
<body>

  <span class="series-label" style="left:40px">poster 1</span>
  <span class="series-label" style="left:433px">poster 2</span>
  <span class="series-label" style="left:818px">poster 3</span>

  <!-- Poster 1: price menu -->
  <section class="poster poster--menu">
    <div class="menu-topbar"></div>
    <div class="model-photo--sailor" role="img" aria-label="Blonde pin-up model in a white sailor dress and cap against a green backdrop, resting against the price frame"></div>
    <span class="brand-name">Corvelle</span>

    <div class="menu-frame"></div>
    <p class="now-showing">NOW SHOWING</p>

    <h2 class="menu-heading" style="top:44px">SERVICES</h2>
    <p class="menu-line" style="top:70px">Full Body Application..............$35.00</p>
    <p class="menu-line" style="top:90px">Half Body Application..............$20.00</p>
    <p class="menu-line" style="top:110px">Competition Application..........$50,00</p>
    <p class="menu-line" style="top:130px">Face Only...............................$10.00</p>

    <h2 class="menu-heading" style="top:158px">PACKAGES</h2>
    <p class="menu-line" style="top:184px">4 Tans.... ...... $120.00 (Never Expires)</p>
    <p class="menu-line" style="top:204px">8 Tans ..........$200.00 (Never Expires)</p>
    <p class="menu-line" style="top:224px">Monthly Unlimited...................$95.00</p>

    <h2 class="menu-heading" style="top:252px">SPECIALS</h2>
    <p class="menu-line" style="top:278px">High School Students .............$25.00</p>
    <p class="menu-line" style="top:292px">EVERYDAY!!</p>
    <p class="menu-line" style="top:314px">All Day Every Tuesday.............$25.00</p>
    <p class="menu-line" style="top:336px">New Clients.....$25.00 (First Visit Only)</p>

    <div class="mobile-band">
      <p class="mobile-note">Don't have time to come to us?&nbsp; We also have MOBILE Services!</p>
      <p class="mobile-call">OUR ARTISTS CAN COME TO YOU!</p>
      <p class="party-rate" style="top:49px">In-Home Party Rates (5 people or more)</p>
      <p class="party-rate" style="top:64px">$35.00 per person (Travel Fee Waived)</p>
    </div>
  </section>

  <!-- Poster 2: sunless solution -->
  <section class="poster poster--solution">
    <span class="brand-name">Corvelle</span>
    <h1 class="solution-title solution-title--first">KELVANE</h1>
    <h1 class="solution-title solution-title--second">SOLUTION...</h1>
    <div class="model-photo--clock" role="img" aria-label="Pin-up model in a red corset and black gloves looking in surprise at an alarm clock"></div>
    <div class="solution-band">
      <p style="top:21px">Pressed for time? Try out kelvane sunless solution.</p>
      <p style="top:43px">Rinse In as little as 2 hours</p>
    </div>
  </section>

  <!-- Poster 3: packages -->
  <section class="poster poster--packages">
    <div class="model-photo--binoculars" role="img" aria-label="Pin-up model in a blue apron dress looking through binoculars while holding a laptop"></div>
    <span class="brand-name">Corvelle</span>
    <div class="low-price">
      <p class="low-price-lead">TANS AS<br>LOW AS</p>
      <p class="low-price-amount">$20</p>
    </div>
    <div class="savings-band">
      We offer packages and<br>memberships with<br><strong>UNBELIEVABLE SAVINGS.</strong>
    </div>
  </section>

</body>
</html>
```